318 Diamond & Fastpitch Clinic 2017

Design a flyer that will promote our 2017 summer camp for boys and girls softball.

Weeks of
July 10th - 14th
July 17th - 21st.

Players ages 5 - 11.
Full day = 9:30am - 2:30pm half day = 9:30am - 11:30am.
$295 / full day : $195/ half day

Hosted by "318 Diamond" affiliated with the KV Meteors Touring Baseball & Softball Club and the Pine Hollow Junior League,

Camp Location PHJL, Lane 48C Maple Bluff.

PHone 555-284-7730, email info@318diamond.example

The color should be "Red white and blue color scheme" with dates and location standing out. 318 Logo should be prominent PHJL and Meteors smaller and secondary.

Feel free to use stock photo's if available. visit www.kvmeteors.example for more pictures and there are links for the 2017 summer camp there with possibly some more information.

Target Market(s)

to catch the eye of parents of players ages 5 - 11 already at little league or shopping in local stores

Colors
ec1f27
0355a3
ffffff

Requirements
Must have
• red white and blue design,
• 318 logo and summer camp prominent so it catches the eye and explains what it is right away.
• the meteors and pine hollow logo's a the bottom showing the affiliation.
Nice to have
• stock photo's or something showing players having a great time or a beautiful ballpark
Should not have
• to much clutter or hard to figure out what it's for

```html
<!DOCTYPE html>
<html lang="en">
<head>
<meta charset="utf-8">
<title>318 Diamond Summer Camp</title>
<link rel="stylesheet" href="https://fonts.googleapis.com/css2?family=Graduate&display=swap">
<style>
  :root {
    --red: #ec1f27;
    --blue: #0355a3;
    --navy: #13294b;
    --white: #ffffff;
    --ink: #2a2a2a;
  }
  html, body {
    margin: 0;
    padding: 0;
    width: 800px;
    height: 1200px;
    overflow: hidden;
    background: var(--white);
  }
  .flyer {
    position: relative;
    width: 800px;
    height: 1200px;
    overflow: hidden;
    background: var(--white);
    font-family: "Graduate", serif;
  }
  .ballpark-scene {
    position: absolute;
    left: 0;
    top: 380px;
    width: 800px;
    height: 820px;
    background:
      radial-gradient(ellipse at 50% 20%, rgba(255,255,255,0.95) 0%, rgba(255,255,255,0) 45%),
      radial-gradient(ellipse at 52% 48%, #c98a4e 0%, #b5773f 22%, rgba(181,119,63,0) 40%),
      linear-gradient(180deg, #ffffff 0%, #e9e4d6 12%, #a9a496 30%, #7f7d70 44%, #6f9a3a 56%, #8bb34a 64%, #b0683e 76%, #a25a34 100%);
  }
  .league-mark {
    position: absolute;
    left: 34px;
    top: 60px;
    width: 130px;
    display: flex;
    align-items: center;
    gap: 8px;
    color: var(--navy);
    font-size: 13px;
    line-height: 1.25;
  }
  .league-mark .dot {
    flex: 0 0 22px;
    height: 22px;
    border-radius: 50%;
    background: #3f9b3a;
  }
  .club-mark {
    position: absolute;
    left: 606px;
    top: 35px;
    width: 164px;
    height: 77px;
    background: var(--navy);
    color: var(--white);
    display: flex;
    align-items: center;
    justify-content: center;
    font-size: 24px;
  }
  .hosted-by {
    position: absolute;
    left: 0;
    width: 800px;
    top: 22px;
    margin: 0;
    text-align: center;
    font-size: 22px;
    color: var(--ink);
    letter-spacing: 1px;
  }
  .host-mark {
    position: absolute;
    left: 250px;
    top: 62px;
    width: 300px;
    height: 230px;
    display: flex;
    flex-direction: column;
    align-items: center;
    justify-content: center;
    gap: 10px;
    color: var(--red);
  }
  .host-mark .circle {
    width: 44px;
    height: 44px;
    border-radius: 50%;
    background: var(--blue);
  }
  .host-mark .name-main {
    font-size: 96px;
    line-height: 1;
  }
  .host-mark .name-sub {
    font-size: 24px;
    line-height: 1;
  }
  .headline {
    position: absolute;
    left: 0;
    width: 800px;
    top: 318px;
    margin: 0;
    text-align: center;
    font-size: 80px;
    font-weight: 400;
    color: var(--blue);
    letter-spacing: 1px;
  }
  .week {
    position: absolute;
    top: 424px;
    height: 40px;
    background: var(--red);
    color: var(--white);
    font-size: 28px;
    line-height: 40px;
    text-align: center;
    box-shadow: 5px 5px 0 var(--blue);
    white-space: nowrap;
  }
  .week-one { left: 76px; width: 314px; }
  .week-two { left: 408px; width: 312px; }

  .info-bands {
    position: absolute;
    left: 16px;
    top: 1000px;
    width: 900px;
    height: 180px;
    transform: rotate(-9deg);
    transform-origin: 0 0;
  }
  .band {
    position: absolute;
    white-space: nowrap;
    overflow: hidden;
    box-sizing: border-box;
  }
  .band-location {
    left: 0;
    top: 0;
    width: 860px;
    height: 60px;
    background: var(--red);
    color: var(--white);
    font-size: 26px;
    line-height: 60px;
    padding-left: 18px;
  }
  .band-hours-blue {
    left: 180px;
    top: 60px;
    width: 680px;
    height: 40px;
    background: var(--blue);
    color: var(--white);
    font-size: 16px;
    line-height: 40px;
    padding-left: 14px;
  }
  .band-hours-white {
    left: 0;
    top: 100px;
    width: 580px;
    height: 40px;
    background: var(--white);
    color: var(--red);
    font-size: 14.5px;
    line-height: 40px;
    padding-left: 14px;
  }
  .band-details {
    left: 0;
    top: 144px;
    width: 740px;
    height: 28px;
    background: var(--navy);
    color: var(--white);
    font-size: 12px;
    line-height: 28px;
    padding-left: 14px;
  }
  .band .gap { display: inline-block; width: 22px; }
</style>
</head>
<body>
  <main class="flyer">
    <div class="ballpark-scene" role="img" aria-label="Sunlit ballpark with packed stands, green outfield and red-brown infield dirt, with a leather baseball glove holding a ball in the foreground"></div>

    <div class="league-mark">
      <span class="dot"></span>
      <span>Pine Hollow Junior League</span>
    </div>

    <p class="hosted-by">HOSTED BY</p>

    <div class="host-mark">
      <span class="circle"></span>
      <span class="name-main">318</span>
      <span class="name-sub">DIAMOND</span>
    </div>

    <div class="club-mark">METEORS</div>

    <h1 class="headline">SUMMER CAMP</h1>

    <div class="week week-one">JULY 10TH - 14TH</div>
    <div class="week week-two">JULY 17TH - 21ST</div>

    <div class="info-bands">
      <div class="band band-location">CAMP LOCATION : PHJL, LANE 48C MAPLE BLUFF</div>
      <div class="band band-hours-blue">FULL DAY : 9:30AM - 2:30PM<span class="gap"></span>HALF DAY : 9:30AM - 11:30AM.</div>
      <div class="band band-hours-white">FULL DAY : 9:30AM - 2:30PM<span class="gap"></span>HALF DAY : 9:30AM - 11:30AM.</div>
      <div class="band band-details">AGES 5 - 11<span class="gap"></span>$295 FULL / $195 HALF<span class="gap"></span>555-284-7730<span class="gap"></span>INFO@318DIAMOND.EXAMPLE</div>
    </div>
  </main>
</body>
</html>
```